COMPANY NAME ------ Velmora82 Brands, Inc. TAGLINE......... It's Splendor!

I need Graphic design for Coconut oil Skincare products!
I need a graphic design that portrays LUXURY AS APPLIED TO MY COMPANY AND THE TAGLINE ! UPSCALE!!
COLOR LAYOUT ................. GOLD ON BLACK, GOLD ON CHOCOLATE LIKE COLOR!
The designers can focus their graphic design based more the word.." "LUXURY"..... The logo I submitted is the two logo I picked.. the logo and the slogan has to be incorporated in the graphic design... The label has to be "ELEGANT" and " UPSCALE".. It can also be "BOLD".

Target Market(s)

20 - 45 years

Industry/Entity Type

Graphic Design

Font styles to use
Decorative

Requirements
Must have
• Luxury feel to it....
Nice to have
• Logo on the label and oil pouring from inside Coconuts !
Should not have
• Local or Country feel because of the word Coconut oil

```html
<!DOCTYPE html>
<html lang="en">
<head>
<meta charset="utf-8">
<title>Velmora82 Coconut Oil Label</title>
<link href="https://fonts.googleapis.com/css2?family=Poiret+One&family=Quicksand:wght@600;700&display=swap" rel="stylesheet">
<style>
  :root {
    --canvas: #ffffff;
    --chocolate: #2c0e07;
    --chocolate-soft: #3a150b;
    --gold: #e6c47c;
    --gold-light: #fbe7b0;
    --gold-deep: #b8873d;
  }
  * { margin: 0; padding: 0; box-sizing: border-box; }
  html, body {
    width: 1200px;
    height: 1200px;
    overflow: hidden;
    background: var(--canvas);
  }
  .label {
    position: absolute;
    left: 240px;
    top: 60px;
    width: 720px;
    height: 1080px;
    background: var(--chocolate);
    text-align: center;
  }
  .brand-mark {
    position: absolute;
    left: 0;
    right: 0;
    top: 150px;
    display: flex;
    flex-direction: column;
    align-items: center;
  }
  .brand-emblem {
    width: 150px;
    height: 150px;
    border-radius: 50%;
    border: 3px solid var(--gold);
    margin-bottom: 24px;
  }
  .brand-name {
    font-family: "Quicksand", sans-serif;
    font-weight: 600;
    font-size: 50px;
    line-height: 1;
    color: var(--gold);
    letter-spacing: 1px;
  }
  .tagline {
    font-family: "Quicksand", sans-serif;
    font-weight: 700;
    font-size: 21px;
    color: var(--gold);
    margin-top: 18px;
  }
  .product-name {
    position: absolute;
    left: 0;
    right: 0;
    top: 455px;
    font-family: "Poiret One", sans-serif;
    font-weight: 400;
    color: var(--gold);
    background: linear-gradient(90deg, var(--gold-deep), var(--gold-light) 45%, var(--gold) 70%, var(--gold-deep));
    -webkit-background-clip: text;
    background-clip: text;
    -webkit-text-fill-color: transparent;
  }
  .product-name .line {
    display: block;
    line-height: 1;
  }
  .product-name .line-main {
    font-size: 118px;
    letter-spacing: 2px;
  }
  .product-name .line-sub {
    font-size: 118px;
    margin-top: -6px;
  }
  .coconut-art {
    position: absolute;
    left: 227px;
    top: 792px;
    width: 266px;
    height: 253px;
    border-radius: 48% 52% 44% 56% / 50% 46% 54% 50%;
    background: radial-gradient(circle at 38% 40%, var(--gold-light), var(--gold) 45%, var(--gold-deep) 100%);
  }
</style>
</head>
<body>
  <main class="label">
    <div class="brand-mark">
      <div class="brand-emblem"></div>
      <div class="brand-name">Velmora82</div>
      <div class="tagline">It's Splendor!</div>
    </div>
    <h1 class="product-name">
      <span class="line line-main">COCONUT</span>
      <span class="line line-sub">OIL</span>
    </h1>
    <div class="coconut-art" role="img" aria-label="Gold illustration of a whole coconut, a halved coconut with oil dripping, and a faceted oil bottle"></div>
  </main>
</body>
</html>
```